Introduction of new dentist and new treatments

We want inform our Patients of our new dentist and new treatment methods. It is dealing about biologic dentistry and holistic dentistry. we are in switzerland and speak german

Font styles to use
Sans Serif

Colors
00a990
33b8a4
9bcb3c
acd036
cadf82
0292cd
3176b5
e34297
e667a6

Requirements
Must have
• Text, which can be edited. It will be in german
• Name of the dental clinic is
• "Velmora - Ihr Zahnarzt in Zug"
Nice to have
• A4 Layout

```html
<!DOCTYPE html>
<html lang="de">
<head>
<meta charset="utf-8">
<title>Velmora – Interdisziplinäre Zahnmedizin</title>
<link rel="stylesheet" href="https://fonts.googleapis.com/css2?family=Source+Sans+3:wght@300;400;600;700&display=swap">
<style>
  :root{
    --teal:#00a990;
    --teal-light:#33b8a4;
    --green:#9bcb3c;
    --lime:#acd036;
    --lime-pale:#cadf82;
    --blue:#0292cd;
    --blue-dark:#3176b5;
    --pink:#e34297;
    --pink-light:#e667a6;
    --text:#555b5f;
    --grey-line:#d9dcde;
    --paper:#ffffff;
  }
  *{box-sizing:border-box;margin:0;padding:0}
  html,body{width:848px;height:1200px;overflow:hidden;background:var(--paper)}
  body{font-family:"Source Sans 3",Arial,sans-serif;color:var(--text)}
  .sheet{position:relative;width:848px;height:1200px;overflow:hidden;background:var(--paper)}
  .decor{position:absolute;left:0;top:0;width:848px;height:1200px}
  .portrait{position:absolute;left:24px;top:0;width:170px;height:178px;border-radius:0 0 85px 85px;
    background:radial-gradient(circle at 50% 40%,#e8c9b4 0%,#d7ac92 35%,#4a7fc0 70%,#2f66a8 100%)}
  .brand{position:absolute;right:42px;top:88px;text-align:center}
  .brand-name{font-size:34px;font-weight:600;letter-spacing:4px;color:var(--blue-dark);text-transform:uppercase;line-height:1}
  .brand-tag{font-size:14px;font-weight:600;color:var(--blue-dark);margin-top:4px}
  .brand-mark{width:14px;height:14px;border-radius:50%;background:var(--pink-light);margin:0 auto 10px}
  .title{position:absolute;left:0;width:848px;top:200px;text-align:center}
  .title-main{font-size:26px;font-weight:700;color:var(--pink);letter-spacing:.5px}
  .title-sub{font-size:27px;font-weight:600;color:var(--teal);line-height:1.2;margin-top:6px}
  .intro{position:absolute;left:70px;width:720px;top:336px;font-size:16px;font-weight:300;line-height:1.45}
  .tab{position:absolute;height:38px;background:var(--teal);border-radius:0 19px 19px 0}
  .tab-left{left:0;top:408px;width:52px}
  .tab-right{left:449px;top:408px;width:44px;border-radius:19px}
  .divider{position:absolute;left:449px;top:418px;width:2px;height:580px;background:var(--teal-light)}
  .section{position:absolute}
  .section h2{font-size:17px;font-weight:600;color:var(--pink);line-height:1.2;margin-bottom:14px}
  .section p{font-size:12.6px;font-weight:300;line-height:1.5}
  .section p strong{font-weight:700;color:#3b4044}
  .col-left{left:78px;width:330px}
  .col-right{left:524px;width:300px}
  .s1{top:412px}.s2{top:413px}.s3{top:692px}.s4{top:692px}
  .s2 p,.s4 p{font-size:12.8px}
  .holistic-label{position:absolute;left:306px;top:966px;width:236px;height:38px;border-radius:19px;
    background:var(--teal);color:#fff;font-size:17px;font-weight:600;display:flex;align-items:center;justify-content:center}
  .holistic-text{position:absolute;left:80px;width:690px;top:1018px;text-align:center;
    font-size:13px;font-weight:300;line-height:1.48;color:var(--teal)}
</style>
</head>
<body>
<main class="sheet">
  <svg class="decor" viewBox="0 0 848 1200" aria-hidden="true">
    <path d="M560 205 C660 175 760 140 848 70 L848 95 C770 160 670 195 560 205Z" fill="var(--grey-line)"/>
    <path d="M470 222 C620 215 760 175 848 120 L848 150 C760 205 620 228 470 222Z" fill="var(--lime-pale)" opacity=".7"/>
    <path d="M10 40 C-5 140 60 200 150 205 C230 208 290 160 310 105 C280 170 210 190 150 182 C80 172 30 120 10 40Z" fill="var(--teal)"/>
    <path d="M0 1080 C250 1150 560 1130 848 1040 L848 1200 L0 1200Z" fill="var(--lime-pale)" opacity=".55"/>
    <path d="M848 1120 L848 1200 L620 1200 C700 1185 780 1160 848 1120Z" fill="var(--teal)"/>
    <path d="M848 1150 L848 1200 L420 1200 C560 1195 720 1180 848 1150Z" fill="var(--green)" opacity=".6"/>
  </svg>

  <div class="portrait" role="img" aria-label="Porträtfoto des neuen Zahnarztes"></div>

  <div class="brand">
    <div class="brand-mark"></div>
    <div class="brand-name">Velmora</div>
    <div class="brand-tag">Ihr Zahnarzt in Zug</div>
  </div>

  <header class="title">
    <h1 class="title-main">INTERDISZIPLINÄRE ZAHNMEDIZIN -</h1>
    <p class="title-sub">Zusammenhang zwischen Zahnproblemen<br>und der Gesundheit von Körper und Geist</p>
  </header>

  <p class="intro">Zahn und Gesundheit haben eins gemeinsam – Man vermisst sie, wenn sie fehlt. Zähne haben einen engen Zusammenhang zur Gesundheit und können diese beeinflussen. Sowohl negativ als auch positiv.</p>

  <div class="tab tab-left"></div>
  <div class="tab tab-right"></div>
  <div class="divider"></div>

  <section class="section col-left s1">
    <h2>Funktion des Kauorgans und<br>interdisziplinäre Zahnmedizin</h2>
    <p>„Funktion ist nicht alles. Aber ohne Funktion ist alles nichts!“ Sagte einst Prof. A. Lindqvist (Zahnarzt, Gnathologie) und betonte die Bedeutung der Funktion des Kausystems. Sprechen, Kauen aber auch Körperhaltung und Stressmanagement gehören zu den Funktionen der Zähne. Ein gut funktionierendes Kauorgan (nach Prof. R. Hallmann, interdisziplinäre Zahnmedizin) kann Stress bewältigen und mehr Leistung und Wohlbefinden bringen. Sehr oft erkennt man Funktionsstörungen daran, dass die Zähne nicht richtig zueinander passen oder Muskelverspannungen und Schmerzen im Kiefergelenk auftreten.</p>
  </section>

  <section class="section col-right s2">
    <h2>Parodontitis und systemische<br>Erkrankungen</h2>
    <p>Parodontitis (Entzündung des Zahnhalteapparats) ist eine der häufigsten chronischen Krankheiten weltweit und daher gut erforscht. Herzkrankheiten, Diabetes und Frühgeburtlichkeit sind einige der systemischen Krankheiten mit der Parodontitis in Zusammenhang steht. <strong>Zahnfleischbulten, Zahnlockerung, Zahnfleischschwund und Zahnverlust sind typische Begleiterscheinungen von Parodontitis.</strong> Eine systematische Parodontitis-Behandlung kann auch positive Auswirkungen auf die gesamte Gesundheit haben.</p>
  </section>

  <section class="section col-left s3">
    <h2>Funktion des Kauorgans und<br>interdisziplinäre Zahnmedizin</h2>
    <p>„Funktion ist nicht alles. Aber ohne Funktion ist alles nichts!“ Sagte einst Prof. A. Lindqvist (Zahnarzt, Gnathologie) und betonte die Bedeutung der Funktion des Kausystems. Sprechen, Kauen aber auch Körperhaltung und Stressmanagement gehören zu den Funktionen der Zähne. Ein gut funktionierendes Kauorgan (nach Prof. R. Hallmann, interdisziplinäre Zahnmedizin) kann Stress bewältigen und mehr Leistung und Wohlbefinden bringen. Sehr oft erkennt man Funktionsstörungen daran, dass die Zähne nicht richtig zueinander passen oder Muskelverspannungen und Schmerzen im Kiefergelenk auftreten.</p>
  </section>

  <section class="section col-right s4">
    <h2>Zahnverlust und neurologische<br>Auswirkung</h2>
    <p>Ein physiologisches Kausystem hat sehr feine Steuerungs- und Wahrnehmungsmöglichkeiten. Bei Zahnverlust werden diese Fähigkeiten weniger benötigt. Weniger gebrauchte Ressourcen werden von der Natur dementsprechend abgebaut. Studien zeigen, dass Menschen mit weniger Zähnen mehr Risiko zur Bildung von Demenz bergen.</p>
  </section>

  <div class="holistic-label">Ganzheitliche Erklärungen</div>
  <p class="holistic-text">Die komplementäre Zahnheilkunde, sehr oft auch als ganzheitliche oder biologische Zahnheilkunde bezeichnet, versucht mit Hilfe von Meridianen (Traditionelle Chinesische Medizin), den Zusammenhang zwischen Zähnen und anderen Organen und Körperteilen zu erklären. Es gibt immer mehr Patienten und Zahnärzte die von dieser Theorie und deren Ergebnissen überzeugt sind. Aufgrund der wissenschaftlichen Lage ist eine ausführliche Aufklärung vor der Behandlung sehr ratsam.</p>
</main>
</body>
</html>
```